Web Design Project

Psychotherapist in Private Practice
Practice name "The Quiet Harbour"
The population is professional adults seeking life coaching and change consultation
I am including a photo for inspiration ONLY - It includes the theme of light and tree branches. There does not HAVE to be a photograph . An illustration , concept or theme of nature /light / generativity / growth / creativity is acceptable
Clean sharp lines Light colors, minimalist , modern.
There is a separate project for a logo design that will become part of the web design
Here are examples of two logos/websites I like
http://www.brightmeadowcentre.ca/
http://www.openridgeadvisors.ca/

Target Market(s)

Professional adults seeking life coaching

Industry/Entity Type

Life Coaching

Requirements
Should not have
• Although the business name has 'compassion' in it, designs with hearts in it would have to be pretty stylish, subtle, mature and sophisticated to be considered.

```html
<!DOCTYPE html>
<html lang="en">
<head>
<meta charset="utf-8">
<title>The Quiet Harbour – Private Psychotherapist</title>
<link href="https://fonts.googleapis.com/css2?family=Roboto+Condensed:wght@300;400;700&family=Roboto:wght@300;400;500&display=swap" rel="stylesheet">
<style>
  :root {
    --brand-blue: #1b75c0;
    --panel-grey: rgba(72, 72, 72, 0.94);
    --nav-grey: rgba(205, 205, 205, 0.85);
    --drop-blue: rgba(40, 120, 185, 0.88);
    --white: #ffffff;
    --ink: #111111;
    --link-blue: #2a8ad8;
    --hero-top: #b7a670;
    --hero-mid: #7f942f;
    --hero-low: #5f6f22;
    --hero-base: #2e3019;
  }
  * { box-sizing: border-box; margin: 0; padding: 0; }
  html, body { width: 1200px; height: 710px; overflow: hidden; }
  body { position: relative; font-family: "Roboto", Arial, sans-serif; background: var(--hero-base); }

  .hero-scene {
    position: absolute; left: 0; top: 0; width: 1200px; height: 653px;
    background: linear-gradient(180deg, var(--hero-top) 0%, var(--hero-mid) 45%, var(--hero-low) 85%, var(--hero-base) 100%);
  }

  .masthead { position: absolute; left: 0; top: 98px; width: 1160px; text-align: center; color: var(--white); }
  .masthead__name { font-family: "Roboto Condensed", Arial, sans-serif; font-weight: 700; font-size: 40px; line-height: 44px; letter-spacing: -1px; }
  .masthead__tagline { font-weight: 300; font-size: 17px; line-height: 20px; margin-top: 4px; margin-left: 10px; }

  .main-nav { position: absolute; left: 600px; top: 214px; width: 400px; height: 31px; display: flex; background: var(--nav-grey); }
  .main-nav__item { width: 95px; text-align: center; font-size: 11.5px; font-weight: 500; color: var(--ink); padding-top: 7px; position: relative; line-height: 14px; }
  .main-nav__item + .main-nav__item::before { content: ""; position: absolute; left: 0; top: 8px; height: 16px; border-left: 1px dotted #888; }
  .main-nav__item--active { width: 115px; background: var(--brand-blue); color: var(--white); border: 1px solid #5aa3e0; }
  .main-nav__chevron { display: block; margin: 1px auto 0; }

  .dropdown { position: absolute; left: 829px; top: 250px; width: 170px; list-style: none; }
  .dropdown__item { height: 26px; margin-bottom: 1px; background: var(--drop-blue); color: var(--white); font-size: 10.5px; font-weight: 300; padding: 7px 0 0 17px; }

  .info-card { position: absolute; top: 430px; width: 264px; height: 206px; box-shadow: 3px 3px 0 var(--white); }
  .info-card--about { left: 203px; background: var(--brand-blue); color: var(--white); padding: 8px 22px; }
  .info-card--contact { left: 486px; background: var(--panel-grey); padding: 12px 30px; }
  .info-card__title { font-family: "Roboto Condensed", Arial, sans-serif; font-weight: 300; font-size: 37px; line-height: 42px; }
  .info-card--contact .info-card__title { color: var(--link-blue); }
  .info-card__text { font-size: 11.2px; font-weight: 300; line-height: 13.5px; margin-top: 4px; }
  .info-card__more { display: block; margin-top: 7px; font-family: "Roboto Condensed", Arial, sans-serif; font-weight: 300; font-size: 11px; color: var(--ink); letter-spacing: -0.3px; }

  .contact-list { list-style: none; margin-top: 12px; }
  .contact-list__item { display: flex; align-items: center; height: 27px; font-size: 12px; font-weight: 300; color: var(--link-blue); }
  .contact-list__icon { width: 24px; margin-right: 18px; }

  .site-footer { position: absolute; left: 0; top: 653px; width: 1200px; height: 57px; background: var(--brand-blue); color: var(--white); }
  .follow { position: absolute; left: 200px; top: 19px; display: flex; align-items: center; font-size: 13px; font-weight: 500; }
  .follow__links { display: flex; gap: 4px; margin-left: 22px; }
  .follow__dot { width: 18px; height: 18px; border-radius: 50%; background: var(--white); }
  .copyright { position: absolute; right: 203px; top: 22px; font-family: "Roboto Condensed", Arial, sans-serif; font-weight: 300; font-size: 10.5px; }
</style>
</head>
<body>
  <div class="hero-scene" role="img" aria-label="Photograph of a sunlit coastal meadow with trees and the sea in soft evening light"></div>

  <header class="masthead">
    <div class="masthead__name">The Quiet Harbour</div>
    <div class="masthead__tagline">Private Psychotherapist</div>
  </header>

  <nav class="main-nav">
    <div class="main-nav__item">Lorem ipsum<svg class="main-nav__chevron" width="8" height="5" viewBox="0 0 8 5"><path d="M1 1l3 3 3-3" fill="none" stroke="#333" stroke-width="1"/></svg></div>
    <div class="main-nav__item">Lorem ipsum<svg class="main-nav__chevron" width="8" height="5" viewBox="0 0 8 5"><path d="M1 1l3 3 3-3" fill="none" stroke="#333" stroke-width="1"/></svg></div>
    <div class="main-nav__item">Lorem ipsum<svg class="main-nav__chevron" width="8" height="5" viewBox="0 0 8 5"><path d="M1 1l3 3 3-3" fill="none" stroke="#333" stroke-width="1"/></svg></div>
    <div class="main-nav__item main-nav__item--active">Lorem ipsum<svg class="main-nav__chevron" width="8" height="8" viewBox="0 0 8 8"><path d="M1 1l3 3 3-3M1 4l3 3 3-3" fill="none" stroke="#fff" stroke-width="1"/></svg></div>
  </nav>

  <ul class="dropdown">
    <li class="dropdown__item">Lorem ipsum dolor sit amet</li>
    <li class="dropdown__item">Lorem ipsum dolor sit amet</li>
    <li class="dropdown__item">Lorem ipsum dolor sit amet</li>
    <li class="dropdown__item">Lorem ipsum dolor sit amet</li>
  </ul>

  <section class="info-card info-card--about">
    <h2 class="info-card__title">About Us</h2>
    <p class="info-card__text">Lorem ipsum dolor sit amet, consectetuer adipiscing elit, sed diam nonummy nibh euismod tincidunt ut laoreet dolore magna aliquam erat volutpat. Ut wisi enim ad minim veniam, quis nostrud exerci tation ullamcorper suscipit lobortis nisl ut aliquip ex ea commodo consequat. Duis autem vel eum iriure dolor ....</p>
    <span class="info-card__more">READ MORE...</span>
  </section>

  <section class="info-card info-card--contact">
    <h2 class="info-card__title">Contact Us</h2>
    <ul class="contact-list">
      <li class="contact-list__item">
        <svg class="contact-list__icon" width="24" height="22" viewBox="0 0 24 22"><path d="M4 2h4v16H4z M3 18q1 3 4 2" fill="none" stroke="#fff" stroke-width="1.6"/><rect x="10" y="3" width="10" height="14" fill="none" stroke="#fff" stroke-width="1.6"/><path d="M12 6h6M12 9h6M12 12h6M12 15h6" stroke="#fff" stroke-width="1.2" stroke-dasharray="1.5 1"/></svg>
        555-0142-0198
      </li>
      <li class="contact-list__item">
        <svg class="contact-list__icon" width="24" height="16" viewBox="0 0 24 16"><rect x="1" y="1" width="22" height="14" fill="#fff"/><path d="M1 1l11 8 11-8M1 15l8-6M23 15l-8-6" fill="none" stroke="#4a4a4a" stroke-width="1.2"/></svg>
        info@quietharbour.ca
      </li>
      <li class="contact-list__item">
        <svg class="contact-list__icon" width="24" height="24" viewBox="0 0 24 24"><g fill="none" stroke="#fff" stroke-width="1.4"><circle cx="12" cy="12" r="10"/><ellipse cx="12" cy="12" rx="4.5" ry="10"/><path d="M2 12h20M4 6.5h16M4 17.5h16M12 2v20"/></g></svg>
        www.quietharbour.ca
      </li>
    </ul>
  </section>

  <footer class="site-footer">
    <div class="follow">
      <span>Follow Us</span>
      <div class="follow__links">
        <span class="follow__dot"></span>
        <span class="follow__dot"></span>
        <span class="follow__dot"></span>
        <span class="follow__dot"></span>
      </div>
    </div>
    <div class="copyright">Copyright © 2013 The Quiet Harbour</div>
  </footer>
</body>
</html>
```